Giving Porter

Need home page design for new website. The winner will have the opportunity to design the entire site.

I have attached 3 files.

1) Sort of a site map. PLEASE do not design the home page based on this wire frame. Be creative and use your expertise.

2) Tagline and Copy for the home page. Please just greek in or make up copy for areas that do not have copy at this time.

3) The logo.
Updates

Hi everyone, I am sorry for the delay. I have been out of town on unexpected business. I will make a decision this week. Thank you all for the great designs. Dale

Industry/Entity Type

Charity

```html
<!DOCTYPE html>
<html lang="en">
<head>
<meta charset="utf-8">
<title>Giving Porter – Home</title>
<link href="https://fonts.googleapis.com/css2?family=Lato:ital,wght@0,400;0,700;1,400&family=Oswald:wght@500&display=swap" rel="stylesheet">
<style>
:root{
  --green:#3db54a;
  --green-dark:#2e9a3b;
  --blue:#1c6f9c;
  --navy:#0f3f74;
  --text:#444;
  --text-dark:#2b2b2b;
  --panel:#ececec;
  --line:#d3d3d3;
  --footer:#1b1b1b;
}
*{box-sizing:border-box;margin:0;padding:0}
html,body{width:1038px;height:1200px;overflow:hidden;background:#fff}
body{font-family:"Lato",sans-serif;color:var(--text);position:relative}
.abs{position:absolute}
.head-font{font-family:"Oswald",sans-serif;font-weight:500}

/* header */
.site-header{left:0;top:0;width:1038px;height:54px;background:linear-gradient(#fafafa,#ececec);border-bottom:1px solid #ddd;z-index:3}
.brand{left:117px;top:4px;display:flex;align-items:center;gap:10px}
.brand-dot{width:82px;height:82px;border-radius:50%;background:#fff;box-shadow:0 2px 4px rgba(0,0,0,.2)}
.brand-name{font-size:27px;color:var(--green);font-weight:400;margin-top:-52px;margin-left:8px}
.main-nav{left:455px;top:0;display:flex;height:54px}
.main-nav a{display:block;padding:0 12px;line-height:54px;font-size:12.5px;font-weight:700;color:#333;text-decoration:none;border-left:1px solid #e2e2e2}
.main-nav a:first-child{border-left:0}
.main-nav a.active{background:linear-gradient(#56c663,var(--green-dark));color:#fff}

/* hero */
.hero{left:0;top:54px;width:1038px;height:406px;background:linear-gradient(180deg,#a9c4d3 0%,#c9d9b5 30%,#7aa23e 62%,#4f7a1f 100%)}
.hero-box{left:576px;top:121px;width:349px;height:203px;background:rgba(25,25,25,.82);border-radius:4px;padding:12px 18px;color:#fff}
.hero-box h1{font-size:25px;color:var(--green);line-height:1.2;margin-bottom:6px}
.hero-box p{font-size:14px;line-height:22px}
.btn-more{display:inline-block;margin-top:10px;background:#1a7fc0;color:#fff;font-size:12px;font-weight:700;padding:5px 9px;border-radius:2px}

/* feature cards */
.feature{width:239px;height:124px;top:403px;background:linear-gradient(#fff,#ebebeb);border-radius:3px;box-shadow:0 0 0 7px rgba(255,255,255,.25),0 6px 8px -4px rgba(0,0,0,.25)}
.feature h2{font-size:17.5px;color:var(--blue);text-align:center;margin:9px 18px 0;padding-bottom:7px;border-bottom:1px dotted #bbb}
.feature .row{display:flex;align-items:center;gap:14px;padding:10px 12px}
.icon-disc{flex:none;width:57px;height:57px;border-radius:50%;background:var(--green);display:flex;align-items:center;justify-content:center}
.feature p{font-size:12px;line-height:18px}

/* welcome */
.welcome{left:114px;top:568px;width:811px;height:243px;background:var(--panel);border-radius:4px}
.video{left:12px;top:10px;width:300px;height:221px;background:#fff;padding:5px;box-shadow:0 1px 3px rgba(0,0,0,.2)}
.video-fill{width:100%;height:100%;background:linear-gradient(135deg,#d9d9d9,#8a8f94 55%,#3a3d42)}
.play{left:147px;top:103px;width:41px;height:41px;border-radius:50%;background:#fff}
.welcome-body{left:332px;top:10px;width:461px}
.welcome-body h2{font-size:22px;color:var(--blue);padding-bottom:6px;border-bottom:1px solid var(--line)}
.welcome-body h2 span{font-family:"Lato",sans-serif;font-weight:400;color:var(--green)}
.welcome-body p{font-size:12px;line-height:19.5px;margin-top:10px}
.welcome-body p+p{margin-top:19px}

/* columns */
.col{top:842px;width:244px}
.col-title{display:flex;align-items:center;gap:9px;height:30px;border-bottom:1px solid var(--line);font-size:20px;color:var(--blue)}
.col-title em{font-style:normal;color:var(--green)}
.quote{margin-top:18px;background:var(--panel);border-radius:8px;padding:10px 14px 14px;font-style:italic;font-size:12px;line-height:18.3px;height:144px}
.quote::before{content:"\201C";font-size:30px;color:#bbb;float:left;line-height:20px;margin-right:3px}
.author{display:flex;align-items:center;gap:20px;margin-top:-16px;margin-left:18px}
.avatar{width:66px;height:66px;border-radius:50%;background:linear-gradient(#d9b8a0,#8a6a55);border:4px solid #fff;box-shadow:0 1px 3px rgba(0,0,0,.3)}
.author span{font-weight:700;font-size:12.5px;color:#333;margin-top:24px}

.event{display:flex;gap:12px;padding:17px 0 12px;border-bottom:1px dotted #bbb}
.event:last-child{border-bottom:0}
.date{flex:none;width:42px;height:48px;text-align:center;color:#fff}
.date b{display:block;height:25px;background:var(--navy);font-size:17px;font-weight:400;line-height:25px}
.date i{display:block;height:23px;background:var(--green);font-style:normal;font-size:11px;line-height:23px;border-bottom:2px solid var(--navy)}
.event h3{font-size:12px;color:#222;margin-top:-3px}
.event p{font-size:11px;line-height:16.5px;color:#333}

.field{margin-top:8px;height:24px;background:#efefef;border:1px solid #d8d8d8;font-size:9.5px;color:#666;padding:6px 8px}
.col form .field:first-child{margin-top:18px}
.field.tall{height:57px}
.submit{float:right;margin-top:10px;background:linear-gradient(#6b6b6b,#444);color:#fff;font-size:12.5px;font-weight:700;padding:5px 10px;border-radius:2px}

.divider{top:846px;width:1px;height:240px;background:linear-gradient(#eee,#ddd,#fff)}

/* footer */
.site-footer{left:0;top:1129px;width:1038px;height:71px;background:linear-gradient(#2e2e2e,#101010);color:#e8e8e8;font-size:11.5px}
.footer-copy{left:114px;top:28px}
.footer-badge{left:470px;top:-15px;width:98px;height:98px;border-radius:50%;background:#f2f2f2}
.social{left:806px;top:22px;display:flex;gap:10px}
.social span{width:22px;height:22px;border-radius:50%;border:2px solid #ddd;background:#555}
</style>
</head>
<body>

<header class="site-header abs">
  <div class="brand abs">
    <div class="brand-dot"></div>
    <div class="brand-name">GivingPorter.com</div>
  </div>
  <nav class="main-nav abs">
    <a href="#">Home</a><a href="#" class="active">Pricing</a><a href="#">Features</a><a href="#">Services</a><a href="#">Products</a><a href="#">About</a><a href="#">Contact</a>
  </nav>
</header>

<section class="hero abs" role="img" aria-label="Gloved hand placing a golf ball on a tee beside an iron club on a sunny fairway"></section>

<div class="hero-box abs">
  <h1 class="head-font">Charity Success, Minus the Stress</h1>
  <p>Thinking about having a charity golf event but are turned off by the stress, hassle, and complexity – relax! GivingPorter.com is your total solution for creating, managing, and successfully completing your event.</p>
  <span class="btn-more">LEARN MORE</span>
</div>

<article class="feature abs" style="left:122px">
  <h2 class="head-font">Raise More, Stress Less</h2>
  <div class="row">
    <div class="icon-disc"><svg width="32" height="30" viewBox="0 0 32 30" fill="#fff"><rect x="2" y="18" width="5" height="10"/><rect x="9" y="14" width="5" height="14"/><rect x="16" y="10" width="5" height="18"/><path d="M3 14 L20 3 L18 1 L26 0 L24 8 L22 5 L5 16Z"/><circle cx="26" cy="24" r="5"/></svg></div>
    <p>Lorem ipsum dolorsit amet consed diay nibh euismodl tincidunt ut laoreet.</p>
  </div>
</article>
<article class="feature abs" style="left:400px">
  <h2 class="head-font">Everything You Need</h2>
  <div class="row">
    <div class="icon-disc"><svg width="34" height="24" viewBox="0 0 34 24"><rect x="1" y="2" width="26" height="19" rx="3" fill="#fff"/><rect x="1" y="7" width="26" height="4" fill="#3db54a"/><path d="M22 15 l4 4 l7 -8" stroke="#fff" stroke-width="2.5" fill="none"/></svg></div>
    <p>Lorem ipsum dolorsit amet consed diay nibh euismodl tincidunt ut laoreet.</p>
  </div>
</article>
<article class="feature abs" style="left:677px">
  <h2 class="head-font">Sold! Silent Auction Module</h2>
  <div class="row">
    <div class="icon-disc"><svg width="32" height="30" viewBox="0 0 32 30" fill="#fff"><rect x="10" y="2" width="12" height="8" rx="1" transform="rotate(35 16 6)"/><rect x="17" y="9" width="4" height="16" transform="rotate(-55 19 17)"/><rect x="2" y="22" width="16" height="3"/><rect x="0" y="26" width="20" height="3"/></svg></div>
    <p>Lorem ipsum dolorsit amet consed diay nibh euismodl tincidunt ut laoreet.</p>
  </div>
</article>

<section class="welcome abs">
  <div class="video abs">
    <div class="video-fill" role="img" aria-label="Video still of a smiling business team in suits standing together"></div>
    <div class="play abs"><svg width="41" height="41" viewBox="0 0 41 41"><path d="M16 12 L29 20.5 L16 29Z" fill="#111"/></svg></div>
  </div>
  <div class="welcome-body abs">
    <h2 class="head-font">Welcome to <span>GivingPorter.com</span></h2>
    <p>Lorem ipsum dolor sit amet, consectetuer adipisemy nibh euismod tincidunt ut laoreetl dolore magna aliquam erat volutpat. Ut wisi enim ad minim veniam quis nostrud exerci tation ullamcorper suscipit lobortis nisl ut aliquip ex ea commodo consequis autem veli eum iriure dolor in hendrerit in vulputate velit esse molestie.</p>
    <p>consequatvel illum dolore eu feugiat nulla facilisis at vero eros et accumsatn usto odiol dignissim qui blandit praesent luptatum zzril delenit augue duis te fcilisi consequatvel illum dolore eu feugiat nulla facilisis at vero eros et accumsatn usto odiol dignissim qui blandit praesent luptatum zzril delenit augue duis te feulla facilisi.</p>
  </div>
</section>

<section class="col abs" style="left:114px">
  <h2 class="col-title head-font"><svg width="20" height="18" viewBox="0 0 20 18" fill="#444"><path d="M0 1h12v8H5l-3 3V9H0z"/><path d="M14 4h6v8h-2v3l-3-3H8v-1h6z"/></svg>Client <em>Testimonials</em></h2>
  <blockquote class="quote">Lorem ipsum dolor sit amet conetuge sed diay nibhdl tincidunt ut laoreet dolore magam er vol wisi enim ad minim veni quis nostrud exerci tationorem ipsum dolor sit ametee sed diammmy nibh eumd tincidunt ut laoreet dolore magna aliqur volpatl</blockquote>
  <div class="author">
    <div class="avatar" role="img" aria-label="Portrait of the client"></div>
    <span>Mr. Tobias Wren</span>
  </div>
</section>

<div class="divider abs" style="left:377px"></div>

<section class="col abs" style="left:397px">
  <h2 class="col-title head-font"><svg width="18" height="18" viewBox="0 0 18 18" fill="none" stroke="#444" stroke-width="1.5"><rect x="1" y="3" width="16" height="14"/><path d="M1 7h16M5 1v4M13 1v4M5 10h2M9 10h2M13 10h1M5 13h2M9 13h2"/></svg>Seminars <em>and Events</em></h2>
  <div class="event"><div class="date"><b>23</b><i>JULY</i></div><div><h3>Lorem ipsum dolor sitak ametn</h3><p>Lorem ipsum dolor sitak amet conset adipiscing elit, euismod poor.</p></div></div>
  <div class="event"><div class="date"><b>20</b><i>JULY</i></div><div><h3>Lorem ipsum dolor sitak ametn</h3><p>Lorem ipsum dolor sitak amet conset adipiscing elit, euismod poor.</p></div></div>
  <div class="event"><div class="date"><b>14</b><i>JULY</i></div><div><h3>Lorem ipsum dolor sitak ametn</h3><p>Lorem ipsum dolor sitak amet conset adipiscing elit, euismod poor.</p></div></div>
</section>

<div class="divider abs" style="left:661px"></div>

<section class="col abs" style="left:681px">
  <h2 class="col-title head-font"><svg width="22" height="16" viewBox="0 0 22 16"><rect x="1" y="1" width="20" height="14" fill="#444"/><path d="M1 1 L11 9 L21 1 M1 15 L8 7 M21 15 L14 7" stroke="#fff" stroke-width="1.3" fill="none"/></svg>Quick <em>Contact Form</em></h2>
  <form>
    <div class="field">First Name</div>
    <div class="field">Phone Number</div>
    <div class="field">Email</div>
    <div class="field tall">Comments</div>
    <span class="submit">SUBMIT</span>
  </form>
</section>

<footer class="site-footer abs">
  <div class="footer-copy abs">© 2014 Giving Porter &nbsp;|&nbsp; All rights reserved</div>
  <div class="footer-badge abs"></div>
  <div class="social abs"><span></span><span></span><span></span><span></span></div>
</footer>

</body>
</html>
```